Visitenkarten-Design für Immobilienmakler
Zielgruppe
Wir sind ein Immobilienmakler.
Aufgabenstellung
Wicht wäre das es im Druckformat geliefert wird, welches von www.Kravendo.de geliefert wird. Ich habe alle möglichen Logo Varianten angehangen.

```html
<!DOCTYPE html>
<html lang="en">
<head>
<meta charset="UTF-8">
<title>Marlow Real Estate – Business Card</title>
<link href="https://fonts.googleapis.com/css2?family=Montserrat:wght@500&family=Roboto+Condensed:wght@400;700&display=swap" rel="stylesheet">
<style>
  :root {
    --stage: #e4e4e2;
    --card-light: #ffffff;
    --card-dark: #262626;
    --ink: #1f2a33;
    --ink-soft: #3a3a3a;
    --orange: #f39a1e;
    --orange-deep: #ea6a1c;
    --paper-text: #f2f2f2;
  }
  * { box-sizing: border-box; margin: 0; padding: 0; }
  html, body {
    width: 1200px; height: 901px; overflow: hidden;
    background: var(--stage);
  }
  .stage {
    width: 1200px; height: 901px;
    display: flex; align-items: center; justify-content: center; gap: 60px;
  }
  .card {
    width: 520px; height: 297px; position: relative;
    box-shadow: 0 6px 20px rgba(0,0,0,.18);
  }
  .card--front { background: var(--card-light); }
  .card--back { background: var(--card-dark); display: flex; align-items: center; justify-content: center; }

  .brand {
    display: flex; align-items: center; gap: 12px;
    font-family: "Montserrat", sans-serif; font-weight: 500;
    letter-spacing: .12em; text-transform: uppercase; white-space: nowrap;
  }
  .brand__dot { width: 16px; height: 16px; border-radius: 50%; background: var(--orange); flex: none; }
  .card--front .brand { position: absolute; top: 74px; left: 150px; font-size: 22px; color: var(--ink); }
  .card--back .brand { font-size: 26px; color: var(--paper-text); }

  .person {
    position: absolute; left: 44px; top: 176px; text-align: right;
    font-family: "Roboto Condensed", sans-serif;
  }
  .person__name { font-size: 27px; font-weight: 700; color: var(--ink-soft); line-height: 1.05; }
  .person__role { font-size: 15px; color: var(--ink-soft); margin-top: 4px; }

  .divider {
    position: absolute; left: 244px; top: 170px; width: 2px; height: 70px;
    background: var(--orange-deep);
  }
  .contacts {
    position: absolute; left: 262px; top: 164px; list-style: none;
    font-family: "Roboto Condensed", sans-serif; font-size: 15px; color: var(--ink-soft);
  }
  .contacts li { display: flex; align-items: center; gap: 10px; height: 26px; }
  .contacts svg { width: 16px; height: 16px; flex: none; }
</style>
</head>
<body>
<main class="stage">
  <section class="card card--front" aria-label="Business card front">
    <div class="brand"><span class="brand__dot"></span>Marlow Real Estate</div>

    <div class="person">
      <p class="person__name">Daniel Hartwell</p>
      <p class="person__role">Owner-Director</p>
    </div>

    <span class="divider"></span>

    <ul class="contacts">
      <li>
        <svg viewBox="0 0 16 16" aria-hidden="true"><path fill="#ea6a1c" d="M3.6 1.5l2.2 2.6-1.3 1.6c.9 2 2.3 3.5 4.2 4.4l1.6-1.3 2.6 2.2-1.3 2.2C6.5 13 3 9.5 1.4 2.8z"/></svg>
        0790 000 418
      </li>
      <li>
        <svg viewBox="0 0 16 16" aria-hidden="true"><rect x="1.5" y="3.5" width="13" height="9" rx="1.5" fill="#ea6a1c"/><path d="M2 4.5l6 4.5 6-4.5" fill="none" stroke="#fff" stroke-width="1.2"/></svg>
        hello@marlowhomes.uk
      </li>
      <li>
        <svg viewBox="0 0 16 16" aria-hidden="true"><circle cx="8" cy="8" r="6.5" fill="#ea6a1c"/><path d="M1.5 8h13M8 1.5c-2.4 3-2.4 10 0 13M8 1.5c2.4 3 2.4 10 0 13" fill="none" stroke="#fff" stroke-width="1"/></svg>
        marlowhomes.co.uk
      </li>
    </ul>
  </section>

  <section class="card card--back" aria-label="Business card back">
    <div class="brand"><span class="brand__dot"></span>Marlow Real Estate</div>
  </section>
</main>
</body>
</html>
```